Open Horizon Table - invitation / brochure

​​I am in need of a bi-fold invitation/brochure for an educational series called "Open Horizon Table". This dinner series provides education and community for "Women in Transition" these are women who are currently getting divorced, recently divorced, or widowed.

I am a partner of a wealth management boutique that advises a small number of high-net-worth families. Additionally, I am married to one of the most prominent family law attorneys in the country. The combination of these two unique perspectives has allowed me to see there is an unfortunate dearth of impactful, powerful, and useful resources to help wealthy women transition from being married to being single. (via divorce and/or death of their spouse)

What, How & WHY I do my job:
As a wealth manager, the "what" and "how" aspects of my job are not materially different from most of my competitors. However, the thing that makes me completely unique, and without competition, is "why" I do my job.

I do this because so many women experience unwelcome and unproductive feelings when the dilution of their marriage is complete AND because there is virtually no good place for them to obtain the important information they truly need to move forward and lead a happy, full, prosperous, productive, and fun life. In the absence of this information, many women experience unwelcome, unpleasant, and unproductive emotions.

For example, some experience shame or fear that they have failed. Others struggle with the belief they wasted a significant portion of their life. Some struggle with unresolved anger over the entire experience. It's very difficult to process and work through these emotions by yourself and it can be hard to get the support and guidance they need from their best friends (most are not trained in this area) may well be married (functional or otherwise) and they often times don't have the times to be there when the newly divorced or widowed women need them most.

Usually, these negative feelings are most intense when they are looking backward in time. However, I have seen women go on and lead remarkably impressive lives. Lives that are ​more ​full, richer, more fun, dynamic, and rewarding than they expected possible.

More about the WHY I do what I do - I created Open Horizon Table so women in transition have a safe, supportive and comfortable space for these women to support each other. While each woman's story is unique, the emotional consequences are fairly common and they do not need to feel alone as they process the sometimes difficult, conflicting, and unpredictable emotions.

I want them to connect with each other because they have a great appreciation and empathy for what all the other women are experiencing. A bi-product of attending and participating in the dinner is to forge friendships and connections with the other woman in attendance so they can be resources to each other when they need help dealing with their own fear, anxiety, or anger. IMPORTANT NOTE - THIS IS NOT A THERAPY OR SUPPORT GROUP. Instead, this is a select group of very successful and accomplished women who have a shared experience and while each is navigating their own path, they have an opportunity to learn important information, in a safe place, where they can share their experience, strength, and hope with each other.

I want the invitation/brochure to feel very bespoke, thoughtfully curated, and specifically designed to address the most important and impactful areas of life, health, and wellness. I want the invitation/brochure to communicate that the presenters are the best in class and thought leaders in their respective areas of expertise. I also want to communicate that they have so much to be excited about. Because they have substantial financial resources, they have a unique opportunity to reinvent themselves and lead a life beyond their wildest dreams. I hope they can see how and why they can stop feeling the negative feelings of anger, sadness, fear, guilt, remorse, and regret. My goal is to get them to look forward (as opposed to backward where the negative emotions come from) so they can be optimistic, excited, happy, joyful, and enthusiastic because they get to be whoever they want; live wherever and however they want. They are not defined nor controlled by their past. They have full control and abundant resources at their disposal to be happier and more fulfilled than they ever hoped or imagined.

The feelings of optimism, excitement, energetic, and joyfulness are very important to the messaging of the Open Horizon Table. I'd like this to be a consistent theme throughout the invitation/brochure. Basically moving from a dark, sad, and negative past to a bright, fun, optimistic, rewarding, fulfilling, and dynamic future.

To create an exciting, rewarding and vibrant life they will want to (in some cases need to) learn new information and skills from the leading authorities in the most important and impactful areas of life.

The presenters at each dinner will focus on one of the "8 Dimensions of Wellness" so they can make thoughtful and informed decisions without fear, anxiety, and stress.

If you think of marriage as two people sailing a ship or flying a plane, the husband and wife often divide the responsibilities of running their affairs because it's too much for one person to manage all by themselves; besides they have a spouse who can help and often times they have different expertise. For illustration purposes, let's say the husband manages the even-numbered items and the wife manages the odd number of items. Each manages half but together everything is well managed and nothing falls through the cracks.

Post-divorce, the husband and wife now each have their own boat to sail and are responsible for all the items (odd and even-numbered) of their ship.

Unfortunately, these women are having to manage items that she has little to no experience with the even-numbered items the husband used to manage during the marriage. They have to take sole control of complicated matters that have serious and long-lasting consequences. That's great if they do a good job. However, given the scope, scale, and complexity of 7-10 figure net worth chances are they won't have the experience, expertise, intellectual resources, and time to manage all the even and odd numbers optimally.

The format of the Open Horizon Table events will be an intimate dinner conversation, in a private room, at a 5 star restaurant in Chicago. There will be a thoughtfully curated group of 4-10 women at one round table to facilitate an interesting and informative presentation. It will be specifically curated for them and delivered. There is no cost to attend the event and they are welcome to attend as many as they like. I will be covering all the expenses related to dinner, drinks, valet parking, and the speaker or presenter.

Each monthly dinner will focus on 1 of the 8 Dimensions of Wellness:

1. Physical - Physical Activity, Good Nutrition, Sleep, Preventing Illness & Injury, and Managing Chronic Health Conditions.

2. Emotional - Coping Effectively with life and creating satisfying relationships.

3. Social - Developing a sense of connection, belonging, and a well-developed support system.

4. Intellectual - Recognizing one’s creative abilities and finding ways to expand knowledge and skills. Boost cognitive function, stimulate the brain, and fuel learning.

5. Environmental - Occupying pleasant, stimulating environments that support well-being.

6. Spiritual - Expanding a sense of purpose and meaning in life, including one’s morals and ethics. (May or may not involve religious activities). Meditation

7. Vocational - Gaining personal satisfaction and enrichment from one's work (maybe academic or professional). Share your talents, wisdom, and experience.

8. Financial - Satisfaction with current and future financial situations.

I'd like the invitation/brochure to give a general overview of the 8 dimensions of wellness and that each gathering will focus on one of the eight. The presentation will be done by women (some of whom went through a divorce or the death of a spouse) who are widely recognized as experts in their respective fields. The female presenters will be highly qualified and credentialed in their field - this could mean they are MDs or PhDs and/or have decades of experience in their specific area of expertise.

I'd like the invitation to be "timeless" meaning that it doesn't have specific dates, times, or locations included. However, if someone would like more information and details they can call or email me for the specific details of the next couple of dates, topics, locations, and menus. I am also open to having a QR code available on the brochure for them to contact me for additional information. Once they contact my office they will receive I will receive all the detailed information via a PDF so they can RSVP if they would like to attend. My goal is that I don't want the invitation/brochure to expire even though the event details change every month.

I will market the Open Horizon Table program by distributing the invitation/brochures available via therapists, divorce lawyers, and grief counselors that specialize in this demographic of women in transition. They in turn will share the invitation/brochure with their woman in transition clients if they think they would benefit from the program

The look and feel I am going for with the brochure/invitation is high-end, contemporary, carefully curated content for a very special and specific community of high-net-worth women in transition that has the resources to be and do anything they want.

Velmora
Silver Larches
Ottavin
PayRo Onyx Card
Shopping in Paris and London
Flying private
Vacationing in the Riviera & Monaco.
Beautiful people
Multi-generational - kids and grandkids.

The theme, feel, and messaging of the invitation/brochure should be consistent with the concept of moving away from – sadness, fear, regret, failure, and negative. And moving towards – joyful, happy, optimistic, exciting, successful, energetic, and contentment.

This information is intended to be informative, empowering, uplifting, transformational, and helpful - so they can lead a life that is bigger, brighter, and better than they ever dreamed of experiencing.

Target Market(s)

Wealthy woman who are currently getting divorced, recently divorced, or widowed. Generally the women will be mid-fourties and older..

Industry/Entity Type

Financial Services targeting wealthy windows and divorced woman.

Font styles to use
Serif
Sans Serif

Requirements
Must have
• The look and feel I am going for with the brochure/invitation is high-end, contemporary, carefully curated content for a very special and specific community of high-net-worth women in transition that has the resources to be and do anything they want. PLEASE ENSURE 70% OF THE WOMAN IN THE INVITATAION/BROCHURE OF NON-WHITE RACES & ETHNICITIES. The theme, feel, and messaging of the invitation/brochure should be consistent with the concept of moving away from – sadness, fear, regret, failure, and negative. And moving towards – joyful, happy, optimistic, exciting, successful, energetic, and contentment. This information is intended to be informative, empowering, uplifting, transformational, and helpful - so they can lead a life that is bigger, brighter, and better than they ever dreamed of experiencing.

```html
<!DOCTYPE html>
<html lang="en">
<head>
<meta charset="utf-8">
<title>Open Horizon Table – Invitation</title>
<link rel="stylesheet" href="https://fonts.googleapis.com/css2?family=Playfair+Display:ital,wght@0,400;0,500;1,400&family=Archivo:ital,wght@0,400;0,500;1,400&family=Roboto+Condensed:wght@300&family=Kaushan+Script&display=swap">
<style>
  :root {
    --backdrop: #e3e3e3;
    --blush: #f1e3dc;
    --blush-deep: #ead8d0;
    --paper: #f7f7f7;
    --ink: #1d1d1d;
    --ink-soft: #555;
    --sky: #c9dcef;
    --mist: #e2e2e2;
    --qr: #f4f4f4;
  }
  * { box-sizing: border-box; margin: 0; padding: 0; }
  html, body { width: 1200px; height: 900px; overflow: hidden; }
  body {
    background: var(--backdrop);
    display: flex;
    align-items: center;
    justify-content: center;
    font-family: "Archivo", sans-serif;
    color: var(--ink);
  }
  .bifold { display: flex; box-shadow: 0 10px 30px rgba(0,0,0,.12); }
  .panel { width: 420px; height: 600px; position: relative; overflow: hidden; }

  /* Inside / about panel */
  .panel--about {
    background: linear-gradient(160deg, var(--blush-deep), var(--blush));
    padding: 40px 38px 34px 42px;
  }
  .about__title {
    font-family: "Playfair Display", serif;
    font-weight: 500;
    font-size: 27px;
    line-height: 1.15;
    margin-left: 30px;
  }
  .about__body {
    font-size: 9.5px;
    line-height: 1.45;
    font-style: italic;
    margin: 14px 0 0 18px;
    max-width: 330px;
  }
  .keypoints__title {
    font-family: "Playfair Display", serif;
    font-weight: 500;
    font-size: 24px;
    margin: 30px 0 16px 30px;
  }
  .keypoints {
    list-style: none;
    display: grid;
    grid-template-columns: 1fr 1fr;
    column-gap: 30px;
    row-gap: 18px;
    font-size: 9.5px;
    line-height: 1.4;
    font-style: italic;
    margin-left: 12px;
  }
  .keypoints li { position: relative; padding-left: 9px; }
  .keypoints li::before { content: "•"; position: absolute; left: 0; }
  .keypoints li:nth-child(2) { margin-top: 18px; }
  .contact__lead {
    font-family: "Playfair Display", serif;
    font-size: 15px;
    line-height: 1.2;
    margin-top: 40px;
    max-width: 340px;
  }
  .contact__details {
    font-size: 11px;
    letter-spacing: .18em;
    line-height: 1.5;
    margin-top: 22px;
  }
  .qr-slot {
    position: absolute;
    right: 48px;
    bottom: 40px;
    width: 62px;
    height: 62px;
    background: var(--qr);
  }

  /* Cover panel */
  .panel--cover { background: var(--paper); }
  .cover__tagline {
    position: absolute;
    top: 300px;
    font-family: "Archivo", sans-serif;
    font-size: 9px;
    letter-spacing: .12em;
    color: var(--ink-soft);
    white-space: nowrap;
    transform: translate(-50%, -50%) rotate(-90deg);
  }
  .cover__tagline--left { left: 48px; }
  .cover__tagline--right { left: 378px; }
  .cover__art { position: absolute; left: 0; top: 0; }
  .cover__heading {
    position: absolute;
    left: 0; right: 0;
    top: 410px;
    text-align: center;
  }
  .cover__kicker {
    font-family: "Roboto Condensed", sans-serif;
    font-weight: 300;
    font-size: 30px;
    letter-spacing: .02em;
    line-height: 1;
  }
  .cover__script {
    font-family: "Kaushan Script", cursive;
    font-size: 74px;
    line-height: 1;
    margin-top: -4px;
  }
  .cover__label {
    font-size: 12px;
    letter-spacing: .4em;
    margin-top: 12px;
    padding-left: .4em;
  }
</style>
</head>
<body>
  <main class="bifold">
    <section class="panel panel--about">
      <h2 class="about__title">About myself<br>and this program</h2>
      <p class="about__body">The reason I created this program is because I am in a unique situation and see a very unmet need. I am a financial advisor to a small number of ultra high net worth families and I am also married to one of the most prominent family law attorneys in the country. This combination of experience and perspective allowed me to see there is no mechanism to help these wealthy woman as they transition from married (chapter 1) to single (chapter 2) and their circumstances are unique given the complexity of their financial circumstances.</p>

      <h2 class="keypoints__title">Some Keypoints</h2>
      <ul class="keypoints">
        <li>High-end dinner in a private room at a 5 star restaurant in Chicago</li>
        <li>This is an intimate gathering of approximately 4-10 woman</li>
        <li>There is no cost to attend the event and they are welcome to attend as many as they like.</li>
        <li>I will be covering the cost of dinner, drinks, valet parking and speaker/presenter</li>
      </ul>

      <p class="contact__lead">For more information and details they can call or email me for the specific details of the next couple of dates, topics, locations, menu's</p>
      <p class="contact__details">123 456 7890<br>email@address.com<br>www.website.com</p>
      <div class="qr-slot" aria-hidden="true"></div>
    </section>

    <section class="panel panel--cover">
      <svg class="cover__art" width="420" height="600" viewBox="0 0 420 600">
        <defs>
          <linearGradient id="portraitTone" x1="0" y1="0" x2="1" y2="1">
            <stop offset="0" stop-color="#f8efe3"/>
            <stop offset="1" stop-color="#f6e1e4"/>
          </linearGradient>
        </defs>
        <rect class="accent-block" x="95" y="55" width="210" height="150" rx="40" fill="var(--sky)" opacity=".75"/>
        <path class="accent-half" d="M300 365 A80 80 0 0 0 300 525 Z" fill="var(--mist)" transform="rotate(-25 300 445)"/>
        <rect x="110" y="120" width="200" height="250" rx="6" fill="url(#portraitTone)" role="img" aria-label="Single-line drawing of two women's faces with yellow and pink lips and small leaf sprigs"/>
      </svg>
      <span class="cover__tagline cover__tagline--left">CONNECT WITH EACH OTHER</span>
      <span class="cover__tagline cover__tagline--right">CONNECT WITH EACH OTHER</span>
      <header class="cover__heading">
        <p class="cover__kicker">OPEN HORIZON</p>
        <h1 class="cover__script">Table</h1>
        <p class="cover__label">INVITATION</p>
      </header>
    </section>
  </main>
</body>
</html>
```